Business Card Re-Design/Update

We'd like to update out business cards. I've included our current "Style guide" which has the colour scheme of the organisation in it. I've also included the branding files with logos etc in them.

I've also included a copy of one of our existing cards so that you can see how ugly/dated they look. I'd like a fresh modern corporate look.

Target Market(s)

These are for our clients, potential clients, industry contacts - like all business cards

Contact Information for Business Card

Name
Position
Company Address - Level 1, 52 Copperfield Road, Dunmore Qld 4071
Direct Phone
mobile
Email
Website -www.korvelit.com.au
Logo

Colors

Designer to choose colors to be used in the design.

Requirements
Must have
• Main Logo
• Cards will need to be editable to be able to personalize them for each new employee.
Nice to have
• The MapIT, HandIT, KeepIT would be okay to have if they can be sensibly and professionally added to the look without detracting from the main imagery.
• Maybe they could go on the back of the card? will leave this to your creative discretion as to whether/where they fit.
Should not have
• Should not have decorative or script fonts

```html
<!DOCTYPE html>
<html lang="en">
<head>
<meta charset="utf-8">
<title>korvelIT business card</title>
<link rel="stylesheet" href="https://fonts.googleapis.com/css2?family=Arimo:wght@400;700&display=swap">
<style>
  :root {
    --stage: #1c1c1e;
    --brand-red: #d91c24;
    --card-dark: #232325;
    --text-light: #e6e6e6;
    --text-muted: #9a9a9c;
    --rule: #4a4a4d;
    --white: #ffffff;
  }
  * { box-sizing: border-box; margin: 0; padding: 0; }
  html, body {
    width: 1200px; height: 900px; overflow: hidden;
    background: var(--stage);
    font-family: "Arimo", Arial, sans-serif;
  }
  .card {
    position: absolute;
    width: 560px; height: 320px;
    border-radius: 26px;
    box-shadow: 0 14px 34px rgba(0,0,0,.55);
  }
  /* Front */
  .card-front {
    left: 90px; top: 100px;
    background: var(--brand-red);
    display: flex; flex-direction: column; align-items: center; justify-content: center;
    color: var(--white);
  }
  .front-mark {
    width: 52px; height: 52px;
    background: var(--white);
    opacity: .92;
    margin-bottom: 18px;
  }
  .front-wordmark {
    font-size: 66px; font-weight: 400; letter-spacing: -1px;
    color: var(--white); line-height: 1;
  }
  .front-web {
    margin-top: 26px;
    font-size: 15px; letter-spacing: 1px;
  }
  /* Back */
  .card-back {
    left: 550px; top: 470px;
    background: var(--card-dark);
    color: var(--text-light);
  }
  .back-brand {
    position: absolute; right: 40px; top: 36px;
    display: flex; align-items: center; gap: 14px;
  }
  .back-mark { width: 30px; height: 30px; background: var(--brand-red); }
  .back-wordmark { font-size: 40px; color: var(--text-light); line-height: 1; letter-spacing: -0.5px; }
  .back-rule {
    position: absolute; left: 40px; right: 40px; top: 100px;
    height: 1px; background: var(--rule);
  }
  .contact-list {
    position: absolute; right: 40px; top: 118px;
    list-style: none; text-align: right;
    font-size: 14px; line-height: 22px; color: var(--text-light);
  }
  .contact-list li { display: flex; justify-content: flex-end; align-items: center; gap: 8px; }
  .contact-list svg { width: 12px; height: 12px; fill: var(--brand-red); }
  .contact-list .email { margin-top: 12px; }
  .person {
    position: absolute; left: 40px; top: 196px;
  }
  .person-name {
    font-size: 20px; font-weight: 700; color: var(--brand-red);
    letter-spacing: .5px; text-transform: uppercase;
  }
  .person-role { font-size: 15px; color: var(--text-muted); margin-top: 3px; }
  .address {
    position: absolute; left: 40px; bottom: 34px;
    font-size: 15px; line-height: 20px; color: var(--text-muted);
    font-style: normal;
  }
</style>
</head>
<body>
  <section class="card card-front" aria-label="Card front">
    <div class="front-mark"></div>
    <div class="front-wordmark">korvelIT</div>
    <div class="front-web">www.korvelit.com.au</div>
  </section>

  <section class="card card-back" aria-label="Card back">
    <div class="back-brand">
      <div class="back-mark"></div>
      <div class="back-wordmark">korvelIT</div>
    </div>
    <div class="back-rule"></div>

    <ul class="contact-list">
      <li>+61 (0)412 555 019
        <svg viewBox="0 0 12 12" aria-label="mobile"><rect x="3" y="0.5" width="6" height="11" rx="1"/></svg></li>
      <li>+61 (0)7 3555 0142
        <svg viewBox="0 0 12 12" aria-label="phone"><path d="M1 4 Q6 0 11 4 L9 6 L7.5 4.5 L4.5 4.5 L3 6 Z M2 7 H10 V11 H2 Z"/></svg></li>
      <li>+61 (0)7 3555 0148
        <svg viewBox="0 0 12 12" aria-label="fax"><rect x="3" y="0.5" width="6" height="4"/><rect x="1" y="5" width="10" height="6" rx="1"/></svg></li>
      <li class="email">dwhitcombe@korvelit.com.au
        <svg viewBox="0 0 12 12" aria-label="email"><path d="M0.5 2.5 H11.5 V9.5 H0.5 Z" /><path d="M0.5 2.5 L6 7 L11.5 2.5" fill="none" stroke="#232325" stroke-width="1"/></svg></li>
    </ul>

    <div class="person">
      <div class="person-name">Dana Whitcombe</div>
      <div class="person-role">Business Development Manager</div>
    </div>

    <address class="address">
      Level 1, 52 Copperfield Road<br>
      Dunmore Qld 4071
    </address>
  </section>
</body>
</html>
```